Energy Company 8-page Brochure

We are in need of a redesign of our 8-page brochure. Attached is the initial design that does not represent us very well. We are looking for CLEAN/CORPORATE look with a little bit of flair (graphs/charts if applicable).

I prefer white background and our company colors (blue/green) to be the accent colors. Feel free to add additional accent colors to highlight certain areas.

We are in the energy field (not just solar), so please consider the types of images that you will use. Are headquarters is located in Chicago, IL so a great looking picture of the skyline or something similar would work for the front and back cover.

We have additional marketing collateral that we will want to be uniformed once we have the right design.

Good luck, and we look forward to receiving some great designs!

Best Regards,
Rob

Target Market(s)

Small to large businesses (B2B).

Industry/Entity Type

It Company

Colors
ffffff
9bcb3c
0255a3

Requirements
Must have
• Clean design, company colors, specified content and editable files.
Nice to have
• Graphs, charts, highlighted areas where necessary.
Should not have
• Clutter! Please utilized page space appropriately. There is a lot of content, so you need to consider graphics and image placement.

```html
<!DOCTYPE html>
<html lang="en">
<head>
<meta charset="utf-8">
<title>Northline Energy – Brochure Spread</title>
<link href="https://fonts.googleapis.com/css2?family=Open+Sans:wght@400;600;700&display=swap" rel="stylesheet">
<style>
  :root {
    --blue: #0255a3;
    --green: #5a9e2f;
    --green-bright: #9bcb3c;
    --white: #ffffff;
    --ink: #4a4f55;
    --backdrop: #d9dadc;
    --fold: #e6e7e9;
  }
  * { box-sizing: border-box; margin: 0; padding: 0; }
  html, body { width: 1200px; height: 800px; overflow: hidden; }
  body {
    background: var(--backdrop);
    font-family: "Open Sans", Arial, sans-serif;
    color: var(--ink);
    position: relative;
  }
  .spread {
    position: absolute; left: 60px; top: 40px;
    width: 1080px; height: 720px;
    display: flex;
    box-shadow: 0 6px 24px rgba(0,0,0,.18);
  }
  .page { position: relative; width: 540px; height: 720px; background: var(--white); overflow: hidden; }
  .page--right { border-left: 1px solid var(--fold); }

  .hero {
    position: absolute; left: 0; top: 0; width: 540px; height: 330px;
    background: linear-gradient(180deg, #0b3f82 0%, #1f6bc0 55%, #0d4a93 70%, #0a3572 100%);
  }
  .hero-title {
    position: absolute; left: 200px; top: 150px; width: 320px;
    color: var(--white); font-weight: 400; font-size: 30px; line-height: 1.12;
  }

  .offer-box {
    position: absolute; background: var(--green); color: var(--white);
    padding: 18px 14px 18px 16px;
  }
  .offer-box--left { left: 26px; top: 180px; width: 160px; height: 345px; }
  .offer-box--right { left: 70px; top: 15px; width: 140px; padding: 16px 10px 18px 12px; }
  .offer-box h3 {
    font-size: 10px; font-weight: 700; text-transform: uppercase;
    line-height: 1.35; margin-bottom: 14px; letter-spacing: .02em;
  }
  .offer-list { list-style: none; }
  .offer-list li {
    position: relative; padding-left: 12px;
    font-size: 10.5px; line-height: 1.35; margin-bottom: 3px;
  }
  .offer-box--right .offer-list li { font-size: 10px; }
  .offer-list li::before {
    content: ""; position: absolute; left: 0; top: 4px;
    width: 6px; height: 6px; background: var(--white);
  }

  .stat-heading {
    position: absolute; left: 200px; top: 348px; width: 320px;
    color: var(--blue); font-size: 15px; font-weight: 700; line-height: 1.25;
  }
  .columns { position: absolute; display: flex; gap: 14px; }
  .columns--left { left: 200px; top: 405px; width: 325px; }
  .columns--right { left: 226px; top: 182px; width: 298px; }
  .column { flex: 1; }
  .column p { font-size: 10px; line-height: 1.33; margin-bottom: 12px; }
  .columns--right .column p { font-size: 9.5px; line-height: 1.3; margin-bottom: 11px; }
  .lead { color: var(--green); font-weight: 700; text-transform: uppercase; }
  .callout { color: var(--green); font-weight: 700; }

  .page-title {
    position: absolute; left: 226px; top: 26px; width: 300px;
    color: var(--blue); font-size: 27px; font-weight: 400; line-height: 1.12;
  }

  .brand {
    position: absolute; display: flex; align-items: center; gap: 8px;
    font-weight: 600; line-height: 1.05;
  }
  .brand--left { left: 28px; top: 610px; color: var(--blue); font-size: 19px; }
  .brand--right { left: 70px; top: 480px; color: var(--green); font-size: 16px; }
  .brand-mark { flex: none; }
</style>
</head>
<body>
  <main class="spread">
    <section class="page page--left">
      <div class="hero" role="img" aria-label="Photograph of a city skyline at night reflected in water, tinted blue"></div>
      <h2 class="hero-title">We are committed to building trust and maintaining objectivity.</h2>

      <aside class="offer-box offer-box--left">
        <h3>Northline Energy Offers</h3>
        <ul class="offer-list">
          <li>Tenure and Standing in the Energy Marketplace</li>
          <li>Buying Power with our Numerous Suppliers</li>
          <li>Expertise in Energy Pricing Negotiation</li>
          <li>Market Timing</li>
          <li>Energy Risk Management</li>
          <li>Expert and Unbiased Advice</li>
          <li>Supplier Independence</li>
        </ul>
      </aside>

      <h2 class="stat-heading">Annual electricity consumption is nearly 4 trillion kWh in the U.S.</h2>

      <div class="columns columns--left">
        <div class="column">
          <p><span class="lead">Energy deregulation</span> allows Northline Energy to garner a lower price for our customers’ energy usage. NLE negotiates procurement with our multiple, competing energy suppliers to secure the most competitive price possible. The key is in knowing how to navigate the process and get the best price and plan for each client’s particular situation. In working with tens of thousands of clients, NLE’s clients benefit from our purchasing power and market recognition. When</p>
        </div>
        <div class="column">
          <p>suppliers compete for our business, our customers save.</p>
          <p><span class="lead">We secure</span> the most competitive energy prices for your business, manage the price volatility and as importantly, provide Budget Certainty.</p>
          <p class="callout">We sit on the same side of the table as our clients.</p>
        </div>
      </div>

      <div class="brand brand--left">
        <svg class="brand-mark" width="30" height="30" viewBox="0 0 30 30" aria-hidden="true"><circle cx="15" cy="15" r="14" fill="#9bcb3c"/></svg>
        <span>Northline<br>Energy</span>
      </div>
    </section>

    <section class="page page--right">
      <aside class="offer-box offer-box--right">
        <h3>K2 – Efficiency Partners Offers</h3>
        <ul class="offer-list">
          <li>Best-of-Breed Energy Efficiency Products</li>
          <li>Proficiency in Garnering Utility and Tax Rebates</li>
          <li>Best-in-Class Demand Management Solutions</li>
          <li>Vendor-Independent, Choosing What is Best for our Clients</li>
          <li>Expertise in Comprehensive Energy Efficiency Solutions</li>
          <li>Complete In-House Project Management</li>
          <li>Cost-Effective Energy Conservation Measures</li>
        </ul>
      </aside>

      <h1 class="page-title">Best-in-class energy demand and energy reduction solutions for your business.</h1>

      <div class="columns columns--right">
        <div class="column">
          <p><span class="lead">Today’s competitive companies</span> know that “Going Green” is not just beneficial to the environment and their communities – it’s also beneficial to their company’s reputation, value proposition and, when done right, it is beneficial to their bottom line. K2 offers comprehensive solutions to increase our clients’ energy efficiency and save them money.</p>
          <p><span class="lead">As a vendor-independent</span> company clients are assured that we are working for them in choosing the most appropriate partners and vendors for their specific needs. We recommend only best-of-breed products and services for our clients, and in many cases with no out-of pocket costs.</p>
          <p><span class="lead">Our approach starts with</span> an analysis of your facility and proceeds with options that can improve the efficiency of your lighting, HVAC, motors, refrigeration and water.</p>
        </div>
        <div class="column">
          <p><span class="lead">As the saying goes</span>, “timing is everything”. Qualified companies are receiving tax credits, utility rebates, and/or favorable lease terms that make their energy efficiency efforts cash positive from day one. State and federal agencies are currently providing significant tax incentives promoting energy conservation and efficiency solutions. In addition, most local utility companies are providing attractive rebates based on proven documented energy reduction solutions. Our financing can allow for positive cash flow and no out-of-pocket costs, allowing for a positive effect on your bottom line.</p>
          <p><span class="lead">The positive cash flow</span> characteristics combined with the incentives and tax deductions make investments in energy efficiency one of the safest and highest yielding investments in this and any economic climate.</p>
        </div>
      </div>

      <div class="brand brand--right">
        <svg class="brand-mark" width="24" height="24" viewBox="0 0 24 24" aria-hidden="true"><rect width="24" height="24" fill="#0255a3"/></svg>
        <span>K2 Efficiency<br>Partners</span>
      </div>
    </section>
  </main>
</body>
</html>
```